Media kit files

Looking for a cleaner more professional look than what we used in past I need a Slide Show template that will work in both profile and landscape

Although I uploaded the present media kit..I am only looking for a template but this should give you an idea of all the things we will use the template for

Included a few versions of the logo for use

Reason: Didn't realize it was a holiday weekend, plus I will be out next Wed-Sun

Deadline has been extended a week.  Forgot this was a holiday weekend. New Deadline 9/8

Reason: So the finalists can re submit

Target Market(s)

Advertisers and consumer marketers B to B

Industry/Entity Type

Media

Requirements
Must have
• Must have fonts that are available in office
• more like the look of the Page uploaded in profile page...but the template will be mostly used for pages such as the landscape ones I uploaded.
• Red should remain primary color...black and grey secondary

```html
<!DOCTYPE html>
<html lang="en">
<head>
<meta charset="utf-8">
<title>Media Kit Template – Font Variants</title>
<link rel="stylesheet" href="https://fonts.googleapis.com/css2?family=Arimo:wght@400;700&family=Fira+Sans:ital,wght@0,400;0,700;1,400&family=Noto+Sans:ital,wght@0,400;0,700;1,400&display=swap">
<style>
  :root {
    --stage: #232323;
    --paper: #ffffff;
    --brand-red: #c8102e;
    --ink: #111111;
    --body-grey: #555555;
    --muted: #8a8a8a;
    --placeholder: #b8b8b8;
    --frame: #e2e2e2;
    --rule: #3a3a3a;
    --label: #ffffff;
  }
  * { margin: 0; padding: 0; box-sizing: border-box; }
  html, body { width: 1200px; height: 1200px; overflow: hidden; background: var(--stage); }
  body { position: relative; font-family: "Arimo", Arial, sans-serif; }

  .font-note { position: absolute; left: 43px; color: var(--label); }
  .font-note__title { font-size: 26px; font-weight: 400; line-height: 1; }
  .font-note__version { font-size: 14.5px; margin: 6px 0 0 5px; }
  .font-note__family { font-size: 14.5px; margin: 30px 0 0 5px; }
  .font-note__styles { list-style: none; margin: 4px 0 0 14px; color: var(--muted); font-size: 14.5px; line-height: 17px; }

  .slide { position: absolute; left: 240px; width: 720px; height: 451px; background: var(--paper); overflow: hidden; }
  .slide--traverse { top: 58px; font-family: "Fira Sans", sans-serif; }
  .slide--veranda { top: 570px; font-family: "Noto Sans", sans-serif; }

  .page-badge { position: absolute; left: 60px; top: 0; width: 26px; height: 30px; background: var(--brand-red); color: #fff; text-align: center; }
  .page-badge__label { display: block; font-size: 8px; line-height: 10px; padding-top: 2px; }
  .page-badge__num { display: block; font-size: 17px; font-weight: 700; line-height: 17px; }
  .slide__date { position: absolute; left: 90px; top: 21px; font-size: 9.5px; color: #333; letter-spacing: .3px; }
  .slide--veranda .slide__date { font-size: 10px; }
  .slide__section { position: absolute; right: 66px; top: 12px; font-size: 17.5px; color: var(--brand-red); letter-spacing: .3px; }
  .slide--veranda .slide__section { top: 13px; font-size: 16.5px; letter-spacing: .5px; }

  .photo-frame { position: absolute; left: 78px; top: 94px; width: 201px; height: 228px; border: 1px solid var(--frame); background: #fff; padding: 7px; }
  .photo-frame__fill { width: 100%; height: 100%; background: var(--placeholder); display: flex; align-items: center; justify-content: center; color: #f4f4f4; font-family: "Arimo", Arial, sans-serif; font-size: 10px; }

  .column-shadow { position: absolute; left: 302px; top: 64px; width: 10px; height: 280px; background: linear-gradient(90deg, rgba(0,0,0,.07), rgba(0,0,0,0)); -webkit-mask: linear-gradient(180deg, transparent, #000 20%, #000 80%, transparent); mask: linear-gradient(180deg, transparent, #000 20%, #000 80%, transparent); }

  .copy { position: absolute; left: 343px; top: 61px; width: 304px; }
  .copy__heading { font-size: 17.5px; font-weight: 700; color: var(--ink); }
  .copy__lead { margin-top: 56px; font-size: 11.2px; line-height: 14px; color: #222; letter-spacing: .2px; }
  .copy__body { margin-top: 16px; font-size: 8.6px; line-height: 13.6px; color: var(--body-grey); letter-spacing: .25px; }
  .copy__body + .copy__body { margin-top: 13.6px; }
  .slide--veranda .copy { top: 62px; width: 300px; }
  .slide--veranda .copy__heading { font-size: 18.5px; letter-spacing: .6px; }
  .slide--veranda .copy__lead { margin-top: 55px; font-size: 10.4px; line-height: 13px; letter-spacing: .3px; }
  .slide--veranda .copy__body { font-size: 7.8px; letter-spacing: .3px; }

  .slide__footer { position: absolute; left: 0; right: 0; bottom: 0; height: 82px; }
  .athlete-photo { position: absolute; left: 64px; top: 0; width: 56px; height: 68px; background: linear-gradient(180deg, #c9d3da 0%, #6f8796 55%, #3f5564 100%); }
  .brand-name { position: absolute; left: 136px; top: 44px; font-size: 15px; font-weight: 700; color: var(--ink); letter-spacing: .2px; }
  .slide--veranda .brand-name { font-size: 14px; }
  .footer-divider { position: absolute; left: 290px; top: 42px; width: 1px; height: 20px; background: #cfcfcf; }
  .tagline { position: absolute; left: 306px; top: 47px; font-size: 9.5px; font-style: italic; color: #222; }
  .slide--veranda .tagline { font-size: 10px; }
  .nav-arrows { position: absolute; left: 600px; top: 42px; }
  .footer-bar { position: absolute; left: 0; right: 0; bottom: 0; height: 15px; background: var(--brand-red); border-top: 3px solid var(--ink); }

  .page-rule { position: absolute; left: 38px; top: 1068px; width: 1108px; height: 1px; background: var(--rule); }
  .signoff-brand { position: absolute; left: 62px; top: 1098px; font-family: "Arimo", Arial, sans-serif; font-size: 42px; font-weight: 700; color: #fff; letter-spacing: .5px; }
  .signoff-title { position: absolute; left: 728px; top: 1112px; font-size: 19px; color: #fff; }
</style>
</head>
<body>

  <section class="font-note" style="top:210px">
    <h2 class="font-note__title">System Font</h2>
    <p class="font-note__version">System Version 2000+</p>
    <p class="font-note__family">Traverse Sans</p>
    <ul class="font-note__styles"><li>Reguler</li><li>Bold</li><li>Italic</li></ul>
  </section>

  <section class="font-note" style="top:709px">
    <h2 class="font-note__title">System Font</h2>
    <p class="font-note__version">System Version 95+</p>
    <p class="font-note__family">Veranda Sans</p>
    <ul class="font-note__styles"><li>Reguler</li><li>Bold</li><li>Italic</li></ul>
  </section>

  <article class="slide slide--traverse">
    <div class="page-badge"><span class="page-badge__label">PAGE</span><span class="page-badge__num">2</span></div>
    <p class="slide__date">DATE: 11/09/2013</p>
    <p class="slide__section">COMPANY OVERVIEW</p>
    <div class="photo-frame"><div class="photo-frame__fill" role="img" aria-label="Placeholder area for a company photo">Picture here</div></div>
    <div class="column-shadow"></div>
    <div class="copy">
      <h1 class="copy__heading">About Us</h1>
      <p class="copy__lead">Completely synergize resource sucking relationships via premier niche markets.</p>
      <p class="copy__body">Dynamically procrastinate B2C users after installed base benefits. Dra-matically visualize customer directed convergence without revolutionary ROI.</p>
      <p class="copy__body">Efficiently unleash cross-media information without cross-media value. Quickly maximize timely deliverables for real-time schemas. Dramatically maintain clicks-and-mortar solutions without functional solutions. Profes-sionally cultivate one-to-one customer service with robust ideas. Dynami-cally innovate resource-leveling customer service for state of the art cus-tomer service..</p>
    </div>
    <footer class="slide__footer">
      <div class="athlete-photo" role="img" aria-label="Photo of a golfer mid-swing"></div>
      <span class="brand-name">MERIDIAN SPORTS</span>
      <span class="footer-divider"></span>
      <span class="tagline">Your Company Tagline here</span>
      <svg class="nav-arrows" width="60" height="24" viewBox="0 0 60 24" aria-label="Previous and next slide">
        <path d="M24 3 L10 12 L24 21 Z" fill="none" stroke="#9a9a9a" stroke-width="1.3"/>
        <path d="M42 3 L56 12 L42 21 Z" fill="none" stroke="#9a9a9a" stroke-width="1.3"/>
      </svg>
      <div class="footer-bar"></div>
    </footer>
  </article>

  <article class="slide slide--veranda">
    <div class="page-badge"><span class="page-badge__label">PAGE</span><span class="page-badge__num">2</span></div>
    <p class="slide__date">DATE: 11/09/2013</p>
    <p class="slide__section">COMPANY OVERVIEW</p>
    <div class="photo-frame"><div class="photo-frame__fill" role="img" aria-label="Placeholder area for a company photo">Picture here</div></div>
    <div class="column-shadow"></div>
    <div class="copy">
      <h1 class="copy__heading">About Us</h1>
      <p class="copy__lead">Completely synergize resource sucking relationships<br>via premier niche markets.</p>
      <p class="copy__body">Dynamically procrastinate B2C users after installed base benefits. Dramati-cally visualize customer directed convergence without revolutionary ROI.</p>
      <p class="copy__body">Efficiently unleash cross-media information without cross-media value. Quickly maximize timely deliverables for real-time schemas. Dramatically maintain clicks-and-mortar solutions without functional solutions. Profes-sionally cultivate one-to-one customer service with robust ideas. Dynami-cally innovate resource-leveling customer service for state of the art cus-tomer service..</p>
    </div>
    <footer class="slide__footer">
      <div class="athlete-photo" role="img" aria-label="Photo of a golfer mid-swing"></div>
      <span class="brand-name">MERIDIAN SPORTS</span>
      <span class="footer-divider"></span>
      <span class="tagline">Your Company Tagline here</span>
      <svg class="nav-arrows" width="60" height="24" viewBox="0 0 60 24" aria-label="Previous and next slide">
        <path d="M24 3 L10 12 L24 21 Z" fill="none" stroke="#9a9a9a" stroke-width="1.3"/>
        <path d="M42 3 L56 12 L42 21 Z" fill="none" stroke="#9a9a9a" stroke-width="1.3"/>
      </svg>
      <div class="footer-bar"></div>
    </footer>
  </article>

  <div class="page-rule"></div>
  <p class="signoff-brand">MERIDIAN SPORTS</p>
  <p class="signoff-title">SLIDE SHOW PRESENTATION</p>

</body>
</html>
```